Artificial intelligence, machine learning, and automation company needs a sexy business card design

We need a sleek and sexy business card design for an AI consulting company based in Philadelphia PA. We provide custom machine learning and automation solutions for companies of all shapes and sizes. The primary industries that we serve are pharmaceuticals, engineering, healthcare, and computer software. We would like the designs to be a black business card that uses green as a sleek accent color. The final design should communicate intelligence, cutting edge new-tech, and optimization.

Target Market(s)

C-level and VP level executives of multi-million annual companies. Mostly in Pharma, Healthcare, Real Estate, Retail, and Engineering

Industry/Entity Type

Computer Software

Contact Information for Business Card

Name: Jack Moss
Title: CEO
Cell: 215 604 8293
Email: JackM@quillarcworks.example
Website: www.QuillarcWorks.example

Font styles to use
Sans Serif

Colors

Designer to choose colors to be used in the design.

Requirements
Must have
• 1) Attached Quillarc Logo (either with colors or not/embossed)
• 2) "Artificial Intelligence" "Automation" and "Machine Learning"
• 3) "Quillarc Laboratories" or "Quillarc Works" or "Quillarc"
• 4) Sexy AF.
Nice to have
• Black card / dark card color, "Quillarc Green" accent colors (in attached .ai file), Embossment of logo/name/etc, thick card stock, colored borders (on card sides, not front/back faces)
Should not have
• Should not be bland, or unsexy.

```html
<!DOCTYPE html>
<html lang="en">
<head>
<meta charset="utf-8">
<title>Quillarc Works — Business Card</title>
<link href="https://fonts.googleapis.com/css2?family=Bebas+Neue&family=Montserrat:wght@400&display=swap" rel="stylesheet">
<style>
  :root {
    --backdrop: #2b2e31;
    --card-ink: #0a0a0a;
    --quillarc-green: #52c7b2;
    --signal-cyan: #2ab4da;
    --soft-line: #7fdcd0;
    --deep-teal: #0f4e4a;
  }
  html, body {
    margin: 0;
    width: 1200px;
    height: 1200px;
    overflow: hidden;
    background: var(--backdrop);
  }
  .canvas {
    width: 1200px;
    height: 1200px;
    display: flex;
    flex-direction: column;
    align-items: center;
    justify-content: space-evenly;
  }
  .card {
    width: 900px;
    height: 514px;
    display: block;
    box-shadow: 0 14px 34px rgba(0,0,0,.45);
  }
  .display-type { font-family: "Bebas Neue", "Oswald", sans-serif; }
  .brand-type { font-family: "Montserrat", sans-serif; font-weight: 400; }
</style>
</head>
<body>
<main class="canvas">

  <!-- Card back -->
  <svg class="card card-back" viewBox="0 0 900 514" aria-label="Card back">
    <defs>
      <linearGradient id="arrowFade" x1="0" y1="1" x2="0" y2="0">
        <stop offset="0" stop-color="var(--signal-cyan)"/>
        <stop offset="1" stop-color="var(--soft-line)"/>
      </linearGradient>
    </defs>
    <rect class="card-face" width="900" height="514" fill="var(--card-ink)"/>
    <line class="edge-rule top" x1="40" y1="14" x2="900" y2="14" stroke="var(--signal-cyan)" stroke-width="5"/>
    <line class="edge-rule bottom" x1="0" y1="498" x2="900" y2="498" stroke="var(--signal-cyan)" stroke-width="5"/>
    <polyline class="corner-seven" points="30,52 150,52 0,175" fill="none" stroke="var(--quillarc-green)" stroke-width="12" stroke-linejoin="miter"/>
    <g class="brand-lockup" transform="translate(450 250)">
      <rect class="brand-square" x="-22" y="-78" width="44" height="44" fill="var(--quillarc-green)"/>
      <text class="brand-type" x="0" y="12" text-anchor="middle" font-size="38" letter-spacing="8" fill="var(--quillarc-green)">QUILLARC</text>
      <text class="brand-type" x="0" y="42" text-anchor="middle" font-size="15" letter-spacing="5" fill="var(--quillarc-green)">LABORATORIES</text>
    </g>
    <g class="rise-arrow" fill="none" stroke="url(#arrowFade)" stroke-width="7" stroke-linecap="round">
      <line x1="808" y1="496" x2="835" y2="360"/>
      <path d="M806 392 L835 360 L866 384"/>
    </g>
  </svg>

  <!-- Card front -->
  <svg class="card card-front" viewBox="0 0 900 514" aria-label="Card front">
    <defs>
      <linearGradient id="arcBand" x1="0" y1="1" x2="1" y2="0">
        <stop offset="0" stop-color="var(--signal-cyan)"/>
        <stop offset="1" stop-color="var(--quillarc-green)"/>
      </linearGradient>
    </defs>
    <rect class="card-face" width="900" height="514" fill="var(--card-ink)"/>
    <line class="top-hairline" x1="0" y1="10" x2="360" y2="10" stroke="var(--soft-line)" stroke-width="5"/>
    <path class="corner-arc" d="M372 0 A325 325 0 0 1 0 360" fill="none" stroke="url(#arcBand)" stroke-width="22"/>
    <path class="corner-arc-inner" d="M350 0 A305 305 0 0 1 0 340" fill="none" stroke="var(--deep-teal)" stroke-width="2"/>

    <g class="brand-lockup" transform="translate(165 170)">
      <rect class="brand-square" x="-78" y="-24" width="34" height="34" fill="var(--quillarc-green)"/>
      <text class="display-type" x="-32" y="10" font-size="46" letter-spacing="2" fill="var(--quillarc-green)">QUILLARC</text>
    </g>

    <text class="display-type person-name" x="420" y="150" font-size="86" fill="var(--quillarc-green)">JACK MOSS</text>
    <text class="display-type person-title" x="420" y="200" font-size="44" fill="var(--quillarc-green)">CEO</text>

    <g class="contact-list display-type" font-size="30" fill="var(--quillarc-green)">
      <g class="contact phone">
        <path d="M392 260 q-6 8 0 18 q6 8 14 8 l2 -6 l-6 -4 l-3 3 q-6 -4 -7 -11 l3 -2 l-2 -7 z" />
        <text x="424" y="284">215 604 8293</text>
      </g>
      <g class="contact email">
        <rect x="385" y="310" width="26" height="18" fill="none" stroke="var(--quillarc-green)" stroke-width="3"/>
        <path d="M385 310 L398 321 L411 310" fill="none" stroke="var(--quillarc-green)" stroke-width="3"/>
        <text x="424" y="330">JACKM@QUILLARCWORKS.EXAMPLE</text>
      </g>
      <g class="contact web">
        <rect x="389" y="354" width="18" height="24" rx="9" fill="var(--quillarc-green)"/>
        <text x="424" y="376">WWW.QUILLARCWORKS.EXAMPLE</text>
      </g>
      <g class="contact address">
        <path d="M398 398 a9 9 0 0 1 9 9 q0 7 -9 16 q-9 -9 -9 -16 a9 9 0 0 1 9 -9 z M398 403 a4 4 0 1 0 0.1 0 z" fill-rule="evenodd"/>
        <text x="424" y="422">2750 MARLOW AVE, PHILADELPHIA, PA 19130</text>
      </g>
    </g>

    <g class="return-arrow" fill="none" stroke="var(--deep-teal)" stroke-width="6" stroke-linecap="round" stroke-linejoin="round">
      <line x1="872" y1="292" x2="790" y2="262"/>
      <path d="M808 246 L790 262 L801 284"/>
    </g>

    <path class="corner-arc-lower" d="M690 514 A260 260 0 0 1 900 448" fill="none" stroke="var(--deep-teal)" stroke-width="16"/>
    <path class="corner-arc-lower-line" d="M722 514 A240 240 0 0 1 900 472" fill="none" stroke="var(--quillarc-green)" stroke-width="2" opacity=".6"/>
  </svg>

</main>
</body>
</html>
```